Lakemont Hydro Partners, Inc. Company Brochure

I would like someone to design a brochure that can be handed out to prospective clients. We are a full service water and wastewater operations company that provides services to Municipal Utility Districts and citys. I would like something that is catchy to the eye and reflects a company that prides itself on providing personal service to its clients. We need to revamp our website, that's next, but the website does have a description of our company and services offered. You can find that information at www.lakemonthydropartners.example

```html
<!DOCTYPE html>
<html lang="en">
<head>
<meta charset="utf-8">
<title>Lakemont Hydro Partners, Inc. — Company Brochure</title>
<link rel="stylesheet" href="https://fonts.googleapis.com/css2?family=Open+Sans:wght@400;600;700&display=swap">
<style>
  :root {
    --brand-blue: #3d86c0;
    --brand-blue-dark: #2f6fa3;
    --water-light: #dbe8f2;
    --water-mid: #8fb6d6;
    --water-deep: #2e5f8f;
    --paper: #f3f4f5;
    --paper-shade: #e4e6e8;
    --ink: #3a3d40;
    --white: #ffffff;
    --stage: #d9d9d9;
  }
  * { box-sizing: border-box; margin: 0; padding: 0; }
  html, body {
    width: 1200px; height: 842px; overflow: hidden;
    background: var(--stage);
    font-family: "Open Sans", Arial, sans-serif;
  }
  .spread { position: relative; width: 1200px; height: 842px; }
  .page {
    position: absolute; top: 220px;
    width: 570px; height: 402px; overflow: hidden;
  }

  /* Back cover */
  .back-cover { left: 20px; background: var(--brand-blue); color: var(--white); }
  .back-cover__circle {
    position: absolute; left: 26px; top: 36px;
    width: 330px; height: 330px; border-radius: 50%;
    background: var(--paper);
    display: flex; flex-direction: column; align-items: center; justify-content: center;
    padding: 0 42px; text-align: center;
  }
  .back-cover__circle::after {
    content: ""; position: absolute; inset: 7px;
    border: 1.5px solid var(--brand-blue); border-radius: 50%;
  }
  .back-cover__heading {
    color: var(--brand-blue); font-weight: 600; font-size: 17px;
    letter-spacing: 0.5px; margin-bottom: 8px;
  }
  .back-cover__body {
    color: var(--brand-blue); font-size: 10px; line-height: 1.38;
  }
  .contact {
    position: absolute; right: 18px; top: 222px; width: 184px;
    text-align: right; font-size: 11.5px; line-height: 1.4; font-style: normal;
    white-space: nowrap;
  }
  .contact__label { font-weight: 700; }
  .contact__rule { border: 0; border-top: 1px solid rgba(255,255,255,0.7); margin: 5px 0 4px; }

  /* Front cover */
  .front-cover {
    left: 610px;
    background: linear-gradient(180deg, var(--white) 0%, var(--paper) 60%, var(--paper-shade) 100%);
  }
  .brand {
    position: absolute; left: 44px; top: 46px;
    display: flex; align-items: center; gap: 9px;
  }
  .brand__mark {
    width: 26px; height: 26px; border-radius: 50%;
    background: var(--brand-blue);
  }
  .brand__name { color: var(--ink); font-weight: 700; font-size: 16px; line-height: 1.1; }
  .water-visual {
    position: absolute; left: 30px; right: 0; top: 100px; height: 190px;
    background:
      radial-gradient(ellipse at 70% 40%, var(--water-deep) 0%, transparent 45%),
      linear-gradient(180deg, transparent 0%, var(--water-mid) 35%, var(--water-light) 70%, var(--water-light) 100%);
    -webkit-mask: linear-gradient(90deg, transparent 0%, #000 10%);
            mask: linear-gradient(90deg, transparent 0%, #000 10%);
  }
  .accent-band {
    position: absolute; left: 30px; right: 0; top: 232px; height: 14px;
    background: var(--brand-blue);
  }
  .tagline {
    position: absolute; left: 0; right: 0; top: 300px; height: 34px;
    background: var(--brand-blue); color: var(--white);
    font-weight: 600; font-size: 18px; letter-spacing: 0.6px;
    display: flex; align-items: center; justify-content: center;
  }
  .web {
    position: absolute; left: 0; right: 0; top: 340px;
    text-align: center; font-size: 11.5px; font-weight: 700; color: var(--ink);
  }
  .web span { color: var(--brand-blue); }
  .bottom-band {
    position: absolute; left: 0; right: 0; bottom: 0; height: 38px;
    background: var(--brand-blue);
  }
</style>
</head>
<body>
<main class="spread">

  <section class="page back-cover" aria-label="Back cover">
    <div class="back-cover__circle">
      <h2 class="back-cover__heading">THE CHOICE IS CLEAR</h2>
      <p class="back-cover__body">Lakemont Hydro Partners, Inc. is a leading competitor in the utility operations industry and has achieved this status by maintaining the quality of work and relationships that few companies can offer. Whether you are a District that is currently operated by an outside contract company or a District entertaining the concept, Lakemont Hydro Partners, Inc. would be delighted to present a detailed quote for operations and services. Please contact our office and a representative will discuss the services that are currently available in your area.</p>
    </div>
    <address class="contact">
      <div><span class="contact__label">Office:</span> 281-555-0147</div>
      <div><span class="contact__label">Toll Free:</span> 800-555-0163</div>
      <hr class="contact__rule">
      <div>4820 Lakeshore Road, Suite 210</div>
      <div>Cedar Bend, Texas 77000</div>
    </address>
  </section>

  <section class="page front-cover" aria-label="Front cover">
    <div class="brand">
      <span class="brand__mark"></span>
      <span class="brand__name">Lakemont Hydro<br>Partners Inc.</span>
    </div>
    <div class="water-visual" role="img" aria-label="Photograph of a splashing blue water surface with bubbles"></div>
    <div class="accent-band"></div>
    <h1 class="tagline">A FULL SERVICE OPERATIONS COMPANY</h1>
    <p class="web">www.<span>lakemonthydropartners</span>.example</p>
    <div class="bottom-band"></div>
  </section>

</main>
</body>
</html>
```